Interior Design/ New Construction interior finishes

Interior Design Website

Target Market(s)

Home builders, New Construction, Renovations, Public

Industry/Entity Type

Construction

Coding

Coded - Design and coding required

Number of Pages Required

1 page

Font styles to use
Sans Serif

Colors

Designer to choose colors to be used in the design.

Requirements
Must have
• Section to upload pictures of projects
• Simple and modern design
• Designer 1 details about myself
• Logo
• Upload section for photos for future jobs
Nice to have
• Sections they can click on to see certain rooms in a house
• Decorating, floral arrangements, holiday decorating.
• I have lots of before and after as well. Maybe a section for those.

```html
<!DOCTYPE html>
<html lang="en">
<head>
<meta charset="utf-8">
<title>Kova Designs — Interior Design</title>
<link href="https://fonts.googleapis.com/css2?family=Open+Sans:wght@400;600;700;800&display=swap" rel="stylesheet">
<style>
:root{
  --ink:#1c1c1c;
  --text:#3a3a3a;
  --muted:#9a9a9a;
  --ghost:#efefef;
  --line:#e4e4e4;
  --paper:#ffffff;
  --soft:#f3f3f3;
  --sage:#eef0ec;
  --frame:#8c8c8c;
  --accent:#b9d2e3;
}
*{box-sizing:border-box;margin:0;padding:0}
html,body{width:1200px;height:2970px;overflow:hidden;background:var(--paper)}
body{position:relative;font-family:"Open Sans",Arial,sans-serif;color:var(--text)}
.abs{position:absolute}

/* sidebar */
.sidebar{left:0;top:0;width:192px;height:2970px;border-right:1px solid var(--line);background:var(--paper)}
.brand{display:flex;align-items:center;gap:8px;font-family:"Open Sans",Arial,sans-serif;font-weight:400;color:var(--ink);letter-spacing:1px}
.brand-dot{width:14px;height:14px;border:1.5px solid var(--ink);border-radius:50%;flex:none}
.sidebar .brand{position:absolute;left:22px;top:112px;font-size:19px}
.menu-icon{left:58px;top:200px;width:14px}
.menu-icon span{display:block;height:2px;background:var(--ink);margin-bottom:2px}
.nav{left:52px;top:226px;list-style:none}
.nav li{height:29px;display:flex;align-items:center;font-size:9.5px;font-weight:700;letter-spacing:.6px;color:var(--muted);text-transform:uppercase;padding-left:26px;position:relative;width:106px}
.nav li::before{content:"";position:absolute;left:8px;top:10px;width:9px;height:9px;border-radius:50%;border:1px solid #d5d5d5}
.nav li.active{background:var(--ink);color:#fff;border-radius:12px;height:22px;margin:3px 0 4px}
.nav li.active::before{background:#fff;border-color:#fff;top:6px}

/* hero */
.hero{left:192px;top:0;width:1008px;height:687px;background:linear-gradient(180deg,#ecebe8 0%,#d9d4cc 45%,#a7a9a6 65%,#7f9bb3 85%,#8ea6ba 100%)}
.hero-title{left:242px;top:478px;color:#fff;font-weight:700;line-height:1;text-transform:uppercase}
.hero-title .small{display:block;font-size:36px;font-weight:400;margin-bottom:8px}
.hero-title .big{display:block;font-size:48px}

.btn{display:flex;align-items:center;justify-content:center;background:var(--ink);color:#fff;font-size:10.5px;font-weight:700;letter-spacing:.5px;text-transform:uppercase}
.btn.light{background:var(--soft);color:var(--ink)}

/* sections */
.ghost{font-size:64px;font-weight:800;color:var(--ghost);text-transform:uppercase;white-space:nowrap;line-height:1}
.title{font-size:28px;font-weight:700;color:var(--ink);text-transform:uppercase;white-space:nowrap;line-height:1}
.para{font-size:11.5px;line-height:19.5px;color:var(--text)}
.tags{display:flex;gap:26px;font-size:9.5px;font-weight:700;letter-spacing:.4px;text-transform:uppercase;color:var(--muted)}
.tags span{display:flex;align-items:center;gap:7px}
.tags span::before{content:"";width:7px;height:7px;background:var(--ink)}
.tags span:first-child{color:var(--ink)}
.divider{height:1px;background:var(--line);left:242px;width:809px}
.frame{border:1.5px solid var(--frame)}
.photo{background:linear-gradient(160deg,#cfcfcf,#8d8d8d 60%,#b5b5b5)}
.tab{display:flex;align-items:center;justify-content:center;background:var(--soft);color:var(--ink);font-size:10px;font-weight:700;text-transform:uppercase;height:35px;top:1311px}
.tab.on{background:var(--ink);color:#fff}

.arrow{width:38px;height:36px;display:flex;align-items:center;justify-content:center;top:1800px}
.before-after{left:192px;top:1913px;width:1008px;height:172px;display:flex}
.ba{flex:1;position:relative;border-right:2px solid #fff}
.ba:last-child{border-right:0}
.ba.before{background:linear-gradient(180deg,#f0f0f0,#9c9c9c)}
.ba.after{background:linear-gradient(180deg,#3a3a3a 0%,#e8e8e8 45%,#7b7b7b 100%)}
.label{position:absolute;bottom:26px;height:26px;width:84px;display:flex;align-items:center;justify-content:center;font-size:12px;font-weight:700}
.ba.before .label{right:0;background:#fff;color:var(--ink)}
.ba.after .label{left:0;background:var(--ink);color:#fff}

.profile-box{left:246px;top:2287px;width:390px;height:333px;background:var(--sage);display:flex;align-items:center;justify-content:center}
.profile-box .brand{font-size:34px;letter-spacing:3px}
.profile-box .brand-dot{width:24px;height:24px}
.name{font-size:14px;font-weight:700;color:var(--ink);letter-spacing:.5px}
.role{font-size:10px;color:var(--muted)}

/* footer */
.footer{left:192px;top:2813px;width:1008px;height:157px;background:var(--soft)}
.social{left:67px;top:40px;display:flex;gap:42px}
.social span{width:16px;height:16px;border-radius:50%;background:#444}
.footer .brand{position:absolute;right:200px;top:52px;font-size:19px}
.footer-line{left:65px;top:97px;width:730px;height:1px;background:#bdbdbd}
.copy{left:0;width:1008px;top:120px;text-align:center;font-size:9px;color:#666;letter-spacing:.4px}
</style>
</head>
<body>

<aside class="sidebar abs">
  <div class="brand"><span class="brand-dot"></span>Kova Designs</div>
  <div class="menu-icon abs"><span></span><span></span><span></span></div>
  <ul class="nav abs">
    <li class="active">Home</li>
    <li>About us</li>
    <li>Projects</li>
    <li>New launches</li>
    <li>Gallery</li>
    <li>Our team</li>
    <li>Contact us</li>
  </ul>
</aside>

<section class="hero abs" role="img" aria-label="Bright living room with white tufted sofas, a rustic wood coffee table and a blue patterned rug"></section>
<h1 class="hero-title abs"><span class="small">Welcome to</span><span class="big">Kova Designs</span></h1>
<div class="btn abs" style="left:242px;top:600px;width:273px;height:32px">Learn more about Kova Designs</div>

<!-- about -->
<div class="ghost abs" style="left:240px;top:730px">About Kova Design</div>
<h2 class="title abs" style="left:268px;top:750px">About Kova Designs</h2>
<div class="tags abs" style="left:242px;top:834px"><span>Decorating</span><span>Floral arrangement</span><span>Holiday decorating</span></div>
<p class="para abs" style="left:242px;top:868px;width:405px">Lorem ipsum dolor sit amet, consectetur adipiscing elit, sed do eiusmod tempor incididunt ut labore et dolore magna aliqua. Ut enim ad minim veniam, quis nostrud exercitation ullamco laboris nisi ut aliquip ex ea commodo consequat.Lorem ipsum dolor sit amet, consectetur adipiscing elit, sed do eiusmod tempor.</p>
<p class="para abs" style="left:242px;top:987px;width:405px">Ut enim ad minim veniam, quis nostrud exercitation ullamco laboris</p>
<div class="btn abs" style="left:242px;top:1041px;width:240px;height:26px">Learn more about Kova Designs</div>
<div class="frame abs" style="left:671px;top:752px;width:365px;height:337px"></div>
<div class="photo abs" style="left:687px;top:738px;width:364px;height:333px" role="img" aria-label="Black and white bedroom with tray ceiling, upholstered bed and bench"></div>

<div class="divider abs" style="top:1144px"></div>

<!-- gallery -->
<div class="ghost abs" style="left:240px;top:1196px">Our Projects Gallery</div>
<h2 class="title abs" style="left:268px;top:1216px">Our Projects Gallery</h2>
<div class="frame abs" style="left:260px;top:1323px;width:366px;height:336px"></div>
<div class="photo abs" style="left:246px;top:1309px;width:362px;height:334px" role="img" aria-label="Black and white photo of a brick home exterior with pool and patio"></div>
<div class="tab on abs" style="left:657px;width:97px">Decorating</div>
<div class="tab abs" style="left:758px;width:153px">Floral arrangement</div>
<div class="tab abs" style="left:917px;width:150px">Holiday decorating</div>
<p class="para abs" style="left:657px;top:1392px;width:380px">Lorem ipsum dolor sit amet, consectetur adipiscing elit, sed do eiusmod tempor incididunt ut labore et dolore magna aliqua. Ut enim ad minim veniam, quis nostrud exercitation ullamco laboris nisi ut aliquip ex ea commodo consequat.Lorem ipsum dolor sit amet, consectetur adipiscing elit, sed do eiusmod tempor.</p>
<p class="para abs" style="left:657px;top:1510px;width:380px">Ut enim ad minim veniam, quis nostrud exercitation ullamco laboris nisi ut aliquip ex ea commodo consequat.Lorem ipsum dolor sit amet, consectetur adipiscing elit, sed do eiusmod tempor.</p>
<div class="btn abs" style="left:657px;top:1604px;width:186px;height:26px">Click on to see rooms</div>
<div class="btn light abs" style="left:851px;top:1604px;width:145px;height:26px">Upload pictures</div>

<div class="divider abs" style="top:1734px"></div>

<!-- before & after -->
<div class="ghost abs" style="left:240px;top:1786px">Before &amp; After</div>
<h2 class="title abs" style="left:268px;top:1804px">Before and After</h2>
<div class="arrow abs" style="left:968px;background:var(--soft)"><svg width="10" height="12" viewBox="0 0 10 12"><path d="M7 1 2 6l5 5" fill="none" stroke="#1c1c1c" stroke-width="2"/></svg></div>
<div class="arrow abs" style="left:1012px;background:var(--ink)"><svg width="10" height="12" viewBox="0 0 10 12"><path d="M3 1l5 5-5 5" fill="none" stroke="#fff" stroke-width="2"/></svg></div>
<div class="before-after abs">
  <div class="ba before" role="img" aria-label="Empty living area before renovation"><span class="label">Before</span></div>
  <div class="ba after" role="img" aria-label="Finished kitchen after renovation"><span class="label">After</span></div>
  <div class="ba before" role="img" aria-label="Unfinished kitchen before renovation"><span class="label">Before</span></div>
  <div class="ba after" role="img" aria-label="White kitchen with island after renovation"><span class="label">After</span></div>
</div>

<!-- about myself -->
<div class="ghost abs" style="left:240px;top:2170px">Myself</div>
<h2 class="title abs" style="left:240px;top:2190px">About Myself</h2>
<div class="frame abs" style="left:260px;top:2303px;width:390px;height:334px"></div>
<div class="profile-box abs"><div class="brand"><span class="brand-dot"></span>Kova Designs</div></div>
<div class="name abs" style="left:701px;top:2321px">EVAN MARLOW</div>
<div class="role abs" style="left:701px;top:2345px">Interior Designer</div>
<p class="para abs" style="left:701px;top:2368px;width:380px">Lorem ipsum dolor sit amet, consectetur adipiscing elit, sed do eiusmod tempor incididunt ut labore et dolore magna aliqua. Ut enim ad minim veniam, quis nostrud exercitation ullamco laboris nisi ut aliquip ex ea commodo consequat.Lorem ipsum dolor sit amet, consectetur adipiscing elit, sed do eiusmod tempor.</p>
<p class="para abs" style="left:701px;top:2490px;width:380px">Ut enim ad minim veniam, quis nostrud exercitation ullamco laboris</p>
<div class="btn abs" style="left:701px;top:2542px;width:208px;height:26px">Learn more about myself</div>

<!-- footer -->
<footer class="footer abs">
  <div class="social abs" aria-label="Social links"><span></span><span></span><span></span><span></span><span></span><span></span></div>
  <div class="brand"><span class="brand-dot"></span>Kova Designs</div>
  <div class="footer-line abs"></div>
  <div class="copy abs">© 2018 INTERIOR DESIGN, ALL RIGHTS RESERVED.</div>
</footer>

</body>
</html>
```